VALMIRA/ VALMIRA GREY Business Card

We have two brands that we would like to show one 1 business card (front and back). We would to incorporate two different logos on one card (VALMIRA and VALMIRA GREY). Card can be two sided. Simple, sleek and professional.

We are a senior living provider.

www.valmira-example.com
www.valmiragrey-example.com

Target Market(s)

Professionals

Industry/Entity Type

Business

Font styles to use
Serif

Colors

Designer to choose colors to be used in the design.

Requirements
Must have
• Space for EMAIL, PHONE, WEBSITE
Nice to have
• Raised lettering or gloss lettering

```html
<!DOCTYPE html>
<html lang="en">
<head>
<meta charset="utf-8">
<title>VALMIRA / VALMIRA GREY – Business Card Design</title>
<link rel="stylesheet" href="https://fonts.googleapis.com/css2?family=Cinzel:wght@500&family=Montserrat:wght@300;400&display=swap">
<style>
  :root {
    --card-black: #1B1917;
    --gold: #CCA859;
    --light-grey: #D6D6D5;
    --charcoal: #2A2A2A;
    --board-top: #8c8c8c;
    --board-bottom: #6f6f6f;
    --white: #ffffff;
  }
  html, body {
    margin: 0;
    padding: 0;
    overflow: hidden;
  }
  .board {
    position: relative;
    width: 1200px;
    height: 1200px;
    overflow: hidden;
    background: linear-gradient(180deg, var(--board-top) 0%, #7d7d7d 45%, var(--board-bottom) 100%);
    font-family: "Montserrat", sans-serif;
  }
  .board-title {
    position: absolute;
    left: 162px;
    top: 30px;
    margin: 0;
    font-family: "Montserrat", sans-serif;
    font-weight: 300;
    font-size: 58px;
    letter-spacing: 0.5px;
    color: var(--white);
  }
  .palette {
    position: absolute;
    top: 124px;
    left: 0;
    width: 1200px;
    height: 42px;
  }
  .swatch {
    position: absolute;
    top: 0;
    display: flex;
    align-items: center;
    gap: 30px;
  }
  .swatch-chip {
    width: 42px;
    height: 42px;
  }
  .swatch-code {
    font-weight: 300;
    font-size: 31px;
    color: var(--white);
  }
  .card {
    position: absolute;
    top: 198px;
    display: block;
  }
  .card--front { left: 25px; }
  .card--back { left: 616px; }
  .card-name {
    font-family: "Cinzel", serif;
    font-weight: 500;
  }
  .card-contact {
    font-family: "Montserrat", sans-serif;
    font-weight: 400;
    font-size: 19px;
    fill: var(--light-grey);
  }
  .card-tagline {
    font-family: "Montserrat", sans-serif;
    font-weight: 300;
    font-size: 21px;
    fill: var(--white);
  }
</style>
</head>
<body>
<main class="board">
  <h1 class="board-title">Business Card design</h1>

  <div class="palette">
    <div class="swatch" style="left:166px"><span class="swatch-chip" style="background:var(--card-black)"></span><span class="swatch-code">1B1917</span></div>
    <div class="swatch" style="left:396px"><span class="swatch-chip" style="background:var(--gold)"></span><span class="swatch-code">CCA859</span></div>
    <div class="swatch" style="left:651px"><span class="swatch-chip" style="background:var(--light-grey)"></span><span class="swatch-code">D6D6D5</span></div>
    <div class="swatch" style="left:890px"><span class="swatch-chip" style="background:var(--charcoal)"></span><span class="swatch-code">2A2A2A</span></div>
  </div>

  <!-- Card front: contact side -->
  <svg class="card card--front" width="560" height="320" viewBox="0 0 700 400" aria-label="VALMIRA business card, contact side">
    <rect class="card-bg" width="700" height="400" fill="var(--card-black)"/>
    <rect class="side-band" x="560" y="0" width="140" height="400" fill="var(--charcoal)"/>
    <line class="side-band-rule" x1="560" y1="0" x2="560" y2="400" stroke="var(--gold)" stroke-width="2"/>
    <rect class="card-frame" x="24" y="24" width="652" height="352" rx="6" fill="none" stroke="var(--gold)" stroke-width="1.2" opacity="0.7"/>

    <rect class="name-mark" x="70" y="76" width="52" height="52" fill="var(--gold)"/>
    <text class="card-name" x="136" y="128" font-size="62" fill="var(--gold)">VALMIRA</text>

    <line class="contact-rule" x1="155" y1="186" x2="155" y2="344" stroke="var(--light-grey)" stroke-width="1.5"/>

    <g class="contact-icon contact-icon--email" transform="translate(110,188)">
      <circle cx="15" cy="15" r="15" fill="none" stroke="var(--gold)" stroke-width="1.5"/>
      <rect x="7" y="10" width="16" height="11" fill="none" stroke="var(--light-grey)" stroke-width="1.4"/>
      <polyline points="7,10 15,16 23,10" fill="none" stroke="var(--light-grey)" stroke-width="1.4"/>
    </g>
    <text class="card-contact" x="164" y="210">Your Email address here</text>

    <g class="contact-icon contact-icon--phone" transform="translate(110,248)">
      <circle cx="15" cy="15" r="15" fill="none" stroke="var(--gold)" stroke-width="1.5"/>
      <path d="M11 8 L14 8 L15 12 L13 13 Q14 17 18 20 L19 18 L22 19 L22 22 Q16 24 11 17 Q8.5 12 11 8 Z" fill="var(--light-grey)"/>
    </g>
    <text class="card-contact" x="164" y="270">Your phone number here</text>

    <g class="contact-icon contact-icon--web" transform="translate(110,310)">
      <circle cx="15" cy="15" r="15" fill="none" stroke="var(--gold)" stroke-width="1.5"/>
      <g fill="none" stroke="var(--light-grey)" stroke-width="1.2">
        <circle cx="15" cy="15" r="8"/>
        <ellipse cx="15" cy="15" rx="3.5" ry="8"/>
        <line x1="7" y1="15" x2="23" y2="15"/>
      </g>
    </g>
    <text class="card-contact" x="164" y="331">Your website here</text>
  </svg>

  <!-- Card back: brand side -->
  <svg class="card card--back" width="564" height="323" viewBox="0 0 705 404" aria-label="VALMIRA GREY business card, brand side">
    <rect class="card-bg" width="705" height="404" fill="var(--card-black)"/>
    <rect class="side-band" x="0" y="0" width="140" height="404" fill="var(--charcoal)"/>
    <line class="side-band-rule" x1="140" y1="0" x2="140" y2="404" stroke="var(--gold)" stroke-width="2"/>
    <rect class="card-frame" x="24" y="24" width="657" height="356" rx="6" fill="none" stroke="var(--gold)" stroke-width="1.2" opacity="0.7"/>

    <rect class="name-mark" x="200" y="180" width="58" height="58" fill="var(--gold)"/>
    <text class="card-name" x="280" y="215" font-size="40" fill="var(--white)" textLength="360" lengthAdjust="spacingAndGlyphs">VALMIRA GREY</text>
    <text class="card-tagline" x="281" y="243" textLength="358" lengthAdjust="spacingAndGlyphs">Executive Personal Care Services</text>
  </svg>
</main>
</body>
</html>
```